The Corwell Laundromat - Pre-Opening Marketing Postcard

We need a design for a 6"x11" postcard that we will use to advertise the upcoming opening of a new laundromat in Baldwin, NY. The name of the store is "The Corwell Laundromat", and the most important things are: match the colors on the card to our logo colors, but also add in some yellow and possibly red accents; say "Free Dryers" in a big, obvious way; include generic washer/dryer pictures, put a basic map of the location on the back of the card, and leave the right 1/3 of the card blank except for the retail indicia and the name "Local Postal Customer". Please refer to the uploaded file showing an example basic layout for the card.
Target Market(s)
low-to-middle-income residents within a 3-mile radius
Industry/Entity Type
Retail
Requirements
Must have
- - The words FREE DRYERS!
- - A simple, hand-drawn map of the location (412 Tansley Road, Baldwin, NY) and major roads nearby (hollis avenue, tansley road, fenwick ave, etc.)
- - The words Opening Soon! (or Opening in March!)
- - The words Newly-Built Laundromat, or New Store!, or something similar
- - The words Local Postal Customer on the back, as shown in my example design layout
- - The retail indicia positioned as shown in my example design layout
- - nothing else on the rear, right-hand 1/3 of the card other than local postal customer and the indicia
Nice to have
- - A transparent background using the generic washers and/or generic dryers pictures
- - Some yellow and red accents or colors to appeal to our hispanic customers
- - The words Professional Wash & Fold Service
Should not have
- - Anything on the back, right-hand 1/3 of the card other than Local Postal Customer and the retail indicia picture

```html
<!DOCTYPE html>
<html lang="en">
<head>
<meta charset="utf-8">
<title>The Corwell Laundromat – Pre-Opening Postcard</title>
<link rel="stylesheet" href="https://fonts.googleapis.com/css2?family=Fredoka:wght@600;700&family=Roboto+Condensed:wght@400;700&family=Montserrat:wght@700&display=swap">
<style>
  :root{
    --page:#e9e6e1;
    --navy:#1d4f96;
    --blue:#2a6fc0;
    --sky:#2b9ad8;
    --red:#d3262b;
    --yellow:#ffe21c;
    --white:#ffffff;
    --mist:#dfe7ee;
    --mint:#b9d3cf;
    --ink:#111111;
  }
  *{box-sizing:border-box;margin:0;padding:0}
  html,body{width:1200px;height:1000px;overflow:hidden}
  body{background:var(--page);position:relative;font-family:"Roboto Condensed",sans-serif}

  .card{position:absolute;overflow:hidden;box-shadow:0 4px 14px rgba(0,0,0,.25)}
  .card-front{left:53px;top:40px;width:795px;height:432px;background:var(--mist)}
  .card-back{left:340px;top:506px;width:793px;height:432px;background:var(--white)}

  .washer-photo{position:absolute;inset:0;background:linear-gradient(180deg,#eef3f7 0%,#d4dde6 55%,#c3ceda 100%)}
  .front-waves{position:absolute;left:0;top:0;width:795px;height:432px}

  .brand{position:absolute;left:37px;top:55px;width:305px;height:290px}
  .brand-disc{position:absolute;inset:0;border-radius:50%;background:var(--mint);opacity:.9}
  .brand-name{position:absolute;inset:0;display:flex;align-items:center;justify-content:center;text-align:center;
    font-family:"Roboto Condensed",sans-serif;font-weight:700;font-size:46px;line-height:1.05;color:var(--navy)}

  .headline{position:absolute;left:412px;top:66px;width:350px;text-align:center;
    font-family:"Fredoka",sans-serif;font-weight:700;font-size:76px;line-height:.98;color:var(--red);
    -webkit-text-stroke:3px var(--yellow);paint-order:stroke fill;letter-spacing:1px}
  .opening{position:absolute;left:420px;top:232px;width:315px;height:46px;background:var(--navy);
    border:2px solid var(--red);border-radius:4px;display:flex;align-items:center;justify-content:center;
    font-family:"Fredoka",sans-serif;font-weight:600;font-size:27px;color:var(--white)}
  .opening .accent{color:var(--yellow);margin-left:7px}

  .front-footer{position:absolute;left:8px;right:8px;top:384px;display:flex;align-items:center;gap:10px;color:var(--white)}
  .front-footer .rule{height:2px;background:var(--white)}
  .front-footer .rule.short{width:55px}
  .front-footer .rule.long{flex:1}
  .front-footer .rule.end{width:28px}
  .tagline{font-weight:700;font-size:25px}
  .address{font-size:19px}

  .back-panel{position:absolute;inset:0}
  .map{position:absolute;left:20px;top:30px;width:410px;height:290px;border-radius:6px;
    background:linear-gradient(160deg,rgba(255,255,255,.14),rgba(255,255,255,.05))}
  .service{position:absolute;left:40px;top:352px;width:340px;text-align:center;color:var(--white)}
  .service-title{font-family:"Montserrat",sans-serif;font-weight:700;font-size:14.5px;letter-spacing:.3px;
    padding-bottom:6px;border-bottom:1px solid var(--white)}
  .service-address{font-size:17px;margin-top:8px}

  .recipient{position:absolute;left:582px;top:150px;transform:rotate(90deg);transform-origin:left top;
    font-family:Arial,sans-serif;font-size:20px;line-height:1.15;color:var(--ink);white-space:nowrap}
  .indicia{position:absolute;left:768px;top:362px;transform:rotate(90deg);transform-origin:left top;
    font-family:Arial,sans-serif;font-weight:700;font-size:7.5px;line-height:1.2;text-align:center;color:var(--ink)}
</style>
</head>
<body>

<section class="card card-front" aria-label="Postcard front">
  <div class="washer-photo" role="img" aria-label="Faded photograph of a row of front-loading washers and dryers"></div>
  <svg class="front-waves" viewBox="0 0 795 432" aria-hidden="true">
    <defs>
      <linearGradient id="band" x1="0" y1="0" x2="0" y2="1">
        <stop offset="0" stop-color="#3aa6e2"/>
        <stop offset="1" stop-color="#1f5aa8"/>
      </linearGradient>
    </defs>
    <path d="M0 295 C150 270 300 330 460 345 C610 358 720 330 795 315 L795 432 L0 432 Z" fill="var(--red)"/>
    <path d="M0 318 C150 292 300 348 460 362 C610 374 720 345 795 333 L795 432 L0 432 Z" fill="url(#band)"/>
  </svg>

  <div class="brand">
    <div class="brand-disc"></div>
    <div class="brand-name">The Corwell<br>Laundromat</div>
  </div>

  <h1 class="headline">FREE DRYERS!</h1>
  <div class="opening">Opening in<span class="accent">March!</span></div>

  <div class="front-footer">
    <span class="rule short"></span>
    <span class="tagline">Newly-Built Laundromat</span>
    <span class="rule long"></span>
    <span class="address">(412 Tansley Road, Baldwin, NY)</span>
    <span class="rule end"></span>
  </div>
</section>

<section class="card card-back" aria-label="Postcard back">
  <svg class="back-panel" viewBox="0 0 793 432" aria-hidden="true">
    <defs>
      <linearGradient id="backBlue" x1="0" y1="1" x2="1" y2="0">
        <stop offset="0" stop-color="#1f4f9c"/>
        <stop offset="1" stop-color="#2fa3dd"/>
      </linearGradient>
    </defs>
    <path d="M0 0 L440 0 C470 40 470 120 445 200 C420 280 420 360 452 432 L0 432 Z" fill="url(#backBlue)"/>
    <path d="M440 0 L458 0 C488 40 486 120 462 200 C438 280 438 360 470 432 L452 432 C420 360 420 280 445 200 C470 120 470 40 440 0 Z" fill="var(--red)"/>
  </svg>

  <div class="map" role="img" aria-label="Simple street map showing 412 Tansley Road with Hollis Avenue, Fenwick Ave and nearby roads, with a location pin"></div>

  <div class="service">
    <div class="service-title">PROFESSIONAL WASH &amp; FOLD SERVICE</div>
    <div class="service-address">(412 Tansley Road, Baldwin, NY)</div>
  </div>

  <div class="recipient">Local Postal<br>Customer</div>
  <div class="indicia">PRSRT STD<br>ECRWSS<br>U.S. POSTAGE<br>PAID<br>EDDM Retail</div>
</section>

</body>
</html>
```